Innovation Presentation Template

I need a unique template design for a presentation on Innovation used exclusively inside of our company. I'd prefer to work in Apple Keynote but can take a .ppt and convert it. The template should appeal to a broad audience of diverse job descriptions. This is a one-time presentation that will last between 30 and 45 minutes. The design should provide a strong visual appeal with multiple chart layouts to support highlighted test points (no bullets, I hate bullets), graphics, line art, and video/photos. My presentations are sparse, never more that 2 concepts per chart (usually one). Our company is a high tech manufacturer selling products in many markets ranging from Government to consumer. The final design should include style a style guide including suggested fonts, colors, graph formats, suggested word art, etc.

Target Market(s)

The audience is internal employees only. Strong corporate branding is not required in this presentation.

Industry/Entity Type

Government

Colors
3277b5
faa54b

Requirements
Must have
• Strong visual appeal helping to support the communication of simple concepts (that have been broken down from complex subject matter).

Multiple chart template forms to support different forms of communication including text points, data charts, graphics, photos, and videos.

Visuals will be memorable, but not overpower the content. Visuals will help convey the content.

Well conceived and coordinated color pallets. Fonts guides (that I can access).

You can visit our company web site at www.vantrel-example.com to see logo and corporate look/feel. It would be good to build logo into a few of the chart templates, but not all.
Nice to have
• Keynote (please). I can live with .ppt if I have to.

Many charts will make a point with simple single sentences. Find a way to make the sentences graphically interesting by varying font and/or color of specific words to help drive points.

Note that colors that I've identified below are based upon the blue used in our logo and the orange that complements it. I'm not married to these but use them as guidelines.
Should not have
• Noise. Corporate nauseia.

```html
<!DOCTYPE html>
<html lang="en">
<head>
<meta charset="utf-8">
<title>Project Title Here</title>
<link href="https://fonts.googleapis.com/css2?family=Open+Sans:wght@400;700&family=Saira+Condensed:wght@500;600;700&family=Saira+Semi+Condensed:wght@500;600;800&display=swap" rel="stylesheet">
<style>
  :root {
    --blue: #1f5fd8;
    --blue-deep: #0b2fa8;
    --blue-light: #2e7be6;
    --orange: #fdb12a;
    --orange-deep: #f7a21b;
    --ink: #4a4a4a;
    --ink-dark: #1b1b1b;
    --box-border: #3a78e0;
    --bg-top: #ffffff;
    --bg-bottom: #e3e6f8;
  }
  * { margin: 0; padding: 0; box-sizing: border-box; }
  html, body { width: 1200px; height: 900px; overflow: hidden; }
  body { font-family: "Open Sans", Arial, sans-serif; }
  .slide {
    position: relative; width: 1200px; height: 900px; overflow: hidden;
    background: linear-gradient(180deg, #f7f8fd 0%, var(--bg-top) 35%, #f0f2fb 70%, var(--bg-bottom) 100%);
  }
  .header { position: absolute; left: 0; top: 0; width: 1200px; height: 80px; }
  .header-band {
    position: absolute; inset: 0;
    background: linear-gradient(90deg, var(--blue-light) 0%, var(--blue) 45%, var(--blue-deep) 85%);
    border-bottom: 2px solid #c9d6f3;
  }
  .header-accent {
    position: absolute; top: 0; right: 0; width: 280px; height: 80px;
    background: linear-gradient(90deg, var(--orange-deep), var(--orange));
    clip-path: polygon(30px 0, 100% 0, 100% 100%, 0 100%);
  }
  .slide-title {
    position: absolute; left: 26px; top: 9px;
    font-family: "Saira Semi Condensed", "Saira Condensed", "Arial Narrow", sans-serif;
    font-weight: 600; font-size: 45px; color: #fff; line-height: 60px;
  }
  .brand {
    position: absolute; right: 16px; top: 18px;
    display: flex; align-items: center; gap: 8px;
  }
  .brand-mark { width: 32px; height: 32px; background: var(--blue-deep); }
  .brand-name {
    font-family: "Saira Semi Condensed", "Saira Condensed", "Arial Narrow", sans-serif;
    font-weight: 800; font-size: 40px; line-height: 44px; color: var(--blue-deep);
    letter-spacing: 1px;
  }
  .steps { position: absolute; left: 50px; top: 204px; }
  .step { position: absolute; left: 0; width: 1093px; height: 146px; }
  .step-marker { position: absolute; left: 0; top: 0; width: 150px; height: 146px; }
  .step-label {
    position: absolute; left: 0; top: 58px; width: 148px; text-align: center;
    color: #fff; font-weight: 700; font-size: 23px;
  }
  .step-box {
    position: absolute; left: 145px; top: 0; width: 948px; height: 97px;
    background: #fff; border: 1.5px solid var(--box-border); border-radius: 6px;
    padding: 9px 0 0 24px;
  }
  .step-line {
    font-size: 24px; line-height: 39px; color: var(--ink); white-space: nowrap;
  }
  .step-line .key { color: var(--blue); font-weight: 700; }
  .step-line .spark { color: var(--orange-deep); font-weight: 700; }
  .footer { position: absolute; left: 0; bottom: 0; width: 1200px; height: 64px; }
  .footer-band { position: absolute; inset: 0; background: linear-gradient(90deg, var(--orange-deep), var(--orange)); }
  .footer-accent {
    position: absolute; left: 0; top: 0; width: 330px; height: 64px;
    background: linear-gradient(90deg, var(--blue-light), var(--blue));
    clip-path: polygon(0 0, 100% 0, 285px 100%, 0 100%);
  }
  .copyright {
    position: absolute; right: 12px; top: 20px;
    font-family: "Saira Semi Condensed", "Saira Condensed", "Arial Narrow", sans-serif;
    font-weight: 500; font-size: 19px; color: var(--ink-dark);
  }
</style>
</head>
<body>
<div class="slide">
  <header class="header">
    <div class="header-band"></div>
    <div class="header-accent"></div>
    <h1 class="slide-title">Project Title Here</h1>
    <div class="brand"><span class="brand-mark"></span><span class="brand-name">VANTREL</span></div>
  </header>

  <section class="steps">
    <div class="step" style="top:0">
      <svg class="step-marker" viewBox="0 0 150 146"><polygon points="0,0 74,26 150,0 150,100 74,146 0,100" fill="#1f5fd8"/></svg>
      <div class="step-label">Text Here</div>
      <div class="step-box">
        <p class="step-line">Every <span class="key">great idea</span> starts as a simple question asked by</p>
        <p class="step-line">someone who refused to accept the <span class="spark">usual answer</span>.</p>
      </div>
    </div>
    <div class="step" style="top:134px">
      <svg class="step-marker" viewBox="0 0 150 146"><polygon points="0,0 74,26 150,0 150,100 74,146 0,100" fill="#1f5fd8"/></svg>
      <div class="step-label">Text Here</div>
      <div class="step-box">
        <p class="step-line">We test early, learn quickly and turn <span class="key">small wins</span> into</p>
        <p class="step-line">lasting change across every team and <span class="spark">every market</span>.</p>
      </div>
    </div>
    <div class="step" style="top:263px">
      <svg class="step-marker" viewBox="0 0 150 146"><polygon points="0,0 74,26 150,0 150,100 74,146 0,100" fill="#1f5fd8"/></svg>
      <div class="step-label">Text Here</div>
      <div class="step-box">
        <p class="step-line">Customers do not buy technology, they buy <span class="key">clear results</span></p>
        <p class="step-line">that make their work safer, faster and <span class="spark">simply better</span>.</p>
      </div>
    </div>
    <div class="step" style="top:399px">
      <svg class="step-marker" viewBox="0 0 150 146"><polygon points="0,0 74,26 150,0 150,100 74,146 0,100" fill="#1f5fd8"/></svg>
      <div class="step-label">Text Here</div>
      <div class="step-box">
        <p class="step-line">Innovation is not one department; it is a <span class="key">shared habit</span></p>
        <p class="step-line">that each of us can practise <span class="spark">starting today</span>.</p>
      </div>
    </div>
  </section>

  <footer class="footer">
    <div class="footer-band"></div>
    <div class="footer-accent"></div>
    <p class="copyright">Copyright text here</p>
  </footer>
</div>
</body>
</html>
```